New Massage Business needs a Card design

We need a card design for our new massage therapy business based in Sydney, Au. The business is getting a makeover, so a little later on we'll need shirts, various pamphlets and promotional flyers, and possibly a website. The winner will be offered those jobs as well.

Colour scheme should be green, black, and steel/charcoal grey. The business focuses on massage as an anatomical solution to stress, muscle aches, pains and fatigue. Ideally we'd like an anatomical image of the muscle system (ref to the attached files). In my mind this image takes up most of the left third of the card, and shows points of tension and pain at the neck and lower back. This image should be the grey portion of the card.

On the upper right is the other image attached, with a simple line drawing of a vehicle on the left end of the line, and a building on the right end replacing the stick figure (we have a therapist specializing in mobile massage). The blank part in the middle of the line should have "Kestrel Wellness", and in smaller writing below, "The Tension Fix".

Bottom right corner should have the contact and business details.
On the back we'd like a "next appointment" and "refer a friend" option.

If you have a design which doesn't fit the above, but you feel suits the business, please submit anyway - sometimes you don't know what you like until you see it.

Business Details:
Name: Kestrel Wellness - The Tension Fix

Industry/Entity Type

Massage Therapy

Contact Information for Business Card

Business Details:
Contact name: Marcus
Title: Massage Therapist
Contact: 0458203617
Email: info@ktfbodywork.example

Requirements
Must have
• Colour scheme should be green, black, and steel/charcoal grey. The business focuses on massage as an anatomical solution to stress, muscle aches, pains and fatigue. Ideally we'd like an anatomical image of the muscle system (ref to the attached files). In my mind this image takes up most of the left third of the card, and shows points of tension and pain at the neck and lower back. This image should be the grey portion of the card.
• On the upper right is the other image attached, with a simple line drawing of a vehicle on the left end of the line, and a building on the right end replacing the stick figure (we have a therapist specializing in mobile massage). The blank part in the middle of the line should have "Kestrel Wellness", and in smaller writing below, "The Tension Fix".
• Bottom right corner should have the contact and business details.
• On the back we'd like a "next appointment" and "refer a friend" option.
Nice to have
• Matt finish - no gloss
• If you have a design which doesn't fit the above, but you feel suits the business, please submit anyway - sometimes you don't know what you like until you see it.
Should not have
• Anything 'Zen'. The business promotes the physiological and scientific benefits of massage. For clients with spiritual or meditative needs, we refer out.

```html
<!DOCTYPE html>
<html lang="en">
<head>
<meta charset="utf-8">
<title>Kestrel Wellness – Business Cards</title>
<link rel="stylesheet" href="https://fonts.googleapis.com/css2?family=Open+Sans:wght@400;600&display=swap">
<style>
  :root {
    --backdrop: #d9d9d9;
    --paper: #f7f7f6;
    --green: #9ccc4a;
    --green-light: #b5d96e;
    --green-deep: #86bb34;
    --charcoal: #4a4a4c;
    --steel: #8a8a8d;
    --ink: #111111;
    --figure-red: #b8432f;
    --figure-tone: #d9826e;
  }
  * { box-sizing: border-box; margin: 0; padding: 0; }
  html, body { width: 1200px; height: 864px; overflow: hidden; }
  body {
    background: var(--backdrop);
    font-family: "Open Sans", Arial, sans-serif;
    color: var(--ink);
    position: relative;
  }
  .card {
    position: absolute;
    left: 240px;
    width: 720px;
    height: 400px;
    overflow: hidden;
    box-shadow: 0 4px 14px rgba(0,0,0,0.18);
  }
  .card--front { top: 22px; background: var(--paper); }
  .card--back {
    top: 442px;
    background: linear-gradient(to bottom, #f4f4f2 0%, #e4eed4 30%, var(--green-light) 65%, var(--green) 100%);
  }
  .card__swoosh { position: absolute; inset: 0; width: 100%; height: 100%; }
  .anatomy-figure {
    position: absolute;
    border-radius: 40% 40% 30% 30%;
    background: radial-gradient(ellipse at 50% 40%, var(--figure-tone) 0%, var(--figure-red) 60%, rgba(184,67,47,0) 75%);
  }
  .card--front .anatomy-figure { left: 220px; top: 18px; width: 210px; height: 270px; }
  .card--back .anatomy-figure { left: 150px; top: 20px; width: 250px; height: 350px; }
  .brand { position: absolute; line-height: 1.05; }
  .brand__name { font-weight: 600; font-size: 44px; letter-spacing: 0.5px; }
  .brand__tagline { font-weight: 400; font-size: 27px; padding-left: 18px; }
  .card--front .brand { left: 420px; top: 128px; }
  .card--back .brand { left: 372px; top: 268px; }
  .contact-person {
    position: absolute;
    right: 424px;
    top: 278px;
    text-align: right;
    line-height: 1.1;
  }
  .contact-person__name { font-weight: 600; font-size: 30px; }
  .contact-person__role { font-size: 21px; }
  .contact-divider {
    position: absolute;
    left: 310px;
    top: 276px;
    width: 2px;
    height: 80px;
    background: var(--ink);
  }
  .contact-list {
    position: absolute;
    left: 326px;
    top: 296px;
    list-style: none;
    font-size: 21px;
    line-height: 1.35;
  }
  .contact-list li { display: flex; align-items: center; gap: 6px; }
  .contact-list svg { width: 17px; height: 17px; flex: none; }
</style>
</head>
<body>
  <section class="card card--front" aria-label="Business card front">
    <svg class="card__swoosh" viewBox="0 0 720 400" preserveAspectRatio="none" aria-hidden="true">
      <path d="M0 205 C 180 225, 360 310, 720 292 L720 400 L0 400 Z" fill="var(--charcoal)"/>
      <path d="M0 222 C 180 240, 360 322, 720 300 L720 400 L0 400 Z" fill="var(--green)"/>
    </svg>
    <div class="anatomy-figure" role="img" aria-label="Anatomical running figure showing the muscle system with highlighted tension points at the joints"></div>
    <div class="brand">
      <div class="brand__name">Kestrel Wellness</div>
      <div class="brand__tagline">The Tension Fix</div>
    </div>
    <div class="contact-person">
      <div class="contact-person__name">Marcus</div>
      <div class="contact-person__role">Massage Therapist</div>
    </div>
    <div class="contact-divider"></div>
    <ul class="contact-list">
      <li>
        <svg viewBox="0 0 16 16" aria-hidden="true"><rect width="16" height="16" rx="2" fill="var(--ink)"/><path d="M5 3 L7 5.5 L6 7 C6.5 8.5 7.5 9.5 9 10 L10.5 9 L13 11 L11.5 13 C7 12.5 3.5 9 3 4.5 Z" fill="var(--green)"/></svg>
        0458203617
      </li>
      <li>
        <svg viewBox="0 0 16 16" aria-hidden="true"><rect width="16" height="16" rx="2" fill="var(--ink)"/><rect x="3" y="4.5" width="10" height="7" fill="none" stroke="var(--green)" stroke-width="1.2"/><path d="M3 4.5 L8 8.5 L13 4.5" fill="none" stroke="var(--green)" stroke-width="1.2"/></svg>
        info@ktfbodywork.example
      </li>
    </ul>
  </section>

  <section class="card card--back" aria-label="Business card back">
    <div class="anatomy-figure" role="img" aria-label="Anatomical running figure showing the muscle system with highlighted tension points at the joints"></div>
    <div class="brand">
      <div class="brand__name">Kestrel Wellness</div>
      <div class="brand__tagline">The Tension Fix</div>
    </div>
  </section>
</body>
</html>
```